Premium Gold Vodka Label Design

English ------------------- We need a label for a Vodka Bottle. Its a sparkling premium vodka with gold inside. The design should look premium. We tried it on our selves but it looks horrible. Therefore we need your help. The current name is corvelle K, but we are open for any better suggestion. We attached the selfmade design. The label will be printed on the bottle. We have other design jobs for you (logo, other sorts)! English ------------------------ We need a label for a vodka bottle. This is a premium vodka which is offset with gold. The design should look like this. We have tried so far and failed. That is why we need your support. The name is so far corvelle K. If you have better suggestions we would be pleased about other suggestions / ideas. In the appendix the failed design is stored. The label is to be applied by screen printing. In the case of good work follow-up projects are guaranteed (logo, other varieties, etc)!
Updates

Reason: We need more time for the decision.

Target Market(s)

USA

Colors

Designer to choose colors to be used in the design.

Requirements
Must have
• English ------------------------ The needed text is on our selfmade label that is attached. English ------------------------ The required texts are stored in the attached design.
Nice to have
• English ------------------------ Transparent places are allowed because we want to print the label on the bottom. English ------------------------ As the label is applied by screen printing, transparent areas are also possible.

```html
<!DOCTYPE html>
<html lang="en">
<head>
<meta charset="utf-8">
<title>Corvelle K Vodka Label</title>
<link rel="stylesheet" href="https://fonts.googleapis.com/css2?family=Cinzel:wght@400;600;700&display=swap">
<style>
  :root {
    --gold: #d39e2c;
    --gold-light: #f6e7c4;
    --brown: #7a3524;
    --label-black: #0b0b0b;
    --stripe: #1b1b1b;
    --ink: #ffffff;
    --dark-ink: #111111;
  }
  html, body {
    margin: 0;
    padding: 0;
    width: 912px;
    height: 1200px;
    overflow: hidden;
    background: #ffffff;
  }
  .label {
    position: relative;
    width: 912px;
    height: 1200px;
    box-sizing: border-box;
    border-radius: 120px;
    background: linear-gradient(135deg, #fbf3e1 0%, var(--gold) 18%, #8a5a2b 45%, var(--brown) 60%, #c8902f 85%, #fbf0d6 100%);
    padding: 26px;
    font-family: "Cinzel", serif;
  }
  .label-face {
    position: relative;
    width: 100%;
    height: 100%;
    border-radius: 96px;
    background: linear-gradient(90deg, var(--label-black), var(--stripe) 50%, var(--label-black));
    border: 2px solid #5a5a5a;
    box-sizing: border-box;
    color: var(--ink);
  }
  .centered {
    position: absolute;
    left: 0;
    right: 0;
    text-align: center;
    margin: 0;
  }
  .brand-band {
    position: absolute;
    left: 89px;
    top: 185px;
    width: 684px;
    height: 112px;
    background: #000000;
    display: flex;
    align-items: center;
    justify-content: center;
  }
  .brand-name {
    font-size: 96px;
    font-weight: 400;
    color: var(--ink);
    letter-spacing: 1px;
    line-height: 1;
  }
  .karat-badge {
    position: absolute;
    left: 314px;
    top: 468px;
    width: 232px;
    height: 96px;
    background: var(--gold);
    display: flex;
    align-items: center;
    justify-content: center;
    color: var(--dark-ink);
    font-size: 64px;
    font-weight: 400;
    line-height: 1;
  }
  .tagline {
    top: 646px;
    font-size: 36px;
    font-weight: 600;
    letter-spacing: 0.5px;
  }
  .product-type {
    top: 700px;
    font-size: 128px;
    font-weight: 400;
    line-height: 1;
  }
  .product-type span {
    background: linear-gradient(90deg, #c98f22 0%, #f8efd8 32%, #c48c3a 55%, #8a4a2c 78%, var(--brown) 100%);
    -webkit-background-clip: text;
    background-clip: text;
    color: transparent;
  }
  .process {
    top: 840px;
    font-size: 46px;
    font-weight: 700;
  }
  .origin {
    top: 972px;
    font-size: 32px;
    font-weight: 400;
  }
  .spec-row {
    position: absolute;
    left: 95px;
    right: 69px;
    top: 1070px;
    display: flex;
    justify-content: space-between;
    align-items: baseline;
  }
  .spec-small {
    font-size: 26px;
    font-weight: 600;
  }
  .spec-volume {
    font-size: 44px;
    font-weight: 600;
    margin-left: 14px;
  }
</style>
</head>
<body>
  <div class="label">
    <div class="label-face">
      <div class="brand-band"><span class="brand-name">CORVELLE K</span></div>
      <div class="karat-badge">24 Kt</div>
      <p class="centered tagline">PREMIUM Gold Sparkling</p>
      <p class="centered product-type"><span>VODKA</span></p>
      <p class="centered process">Distilled 8 Filtered</p>
      <p class="centered origin">Made in Germany</p>
      <div class="spec-row">
        <span class="spec-small">40%Al. Vol.</span>
        <span class="spec-volume">200ML</span>
        <span class="spec-small">80Proof</span>
      </div>
    </div>
  </div>
</body>
</html>
```